Velmora Link5 Business Card

Hi, We need business cards for our sales agents for our business.
Please have a look at the website www.velmoralink5.co and also the attached files for some design expectation and different type of content to be placed on the card.
e.g. Job designation could be - Agent, Zoning Agent or Director. When you submit mock up please submit with variations in the data. Please provide fresh designs and let me know if any questions. Thanks

Industry/Entity Type

Business

```html
<!DOCTYPE html>
<html lang="en">
<head>
<meta charset="utf-8">
<title>Velmora Link5 – Agent Business Card</title>
<link rel="stylesheet" href="https://fonts.googleapis.com/css2?family=Open+Sans:wght@400;700;800&display=swap">
<style>
  :root {
    --page: #ffffff;
    --card-edge: #8a8a8a;
    --navy: #1f2a44;
    --band-dark: #0f2f86;
    --band-light: #2f6fd6;
    --swoosh-orange: #f26a1b;
    --ink: #111111;
    --white: #ffffff;
    --photo-light: #e9ecee;
    --photo-mid: #b9c3c4;
    --photo-water: #5d7f6a;
    --photo-deep: #4e6e5a;
  }
  html, body {
    margin: 0;
    width: 1200px;
    height: 818px;
    overflow: hidden;
    background: var(--page);
  }
  .card {
    position: absolute;
    left: 113px;
    top: 122px;
    width: 987px;
    height: 580px;
    border: 1.5px solid var(--card-edge);
    box-sizing: border-box;
    overflow: hidden;
    background: var(--white);
  }
  .card-art {
    position: absolute;
    inset: 0;
    width: 100%;
    height: 100%;
  }
  .brand-name {
    position: absolute;
    left: 47px;
    top: 60px;
    margin: 0;
    font-family: "Open Sans", sans-serif;
    font-weight: 800;
    font-size: 54px;
    letter-spacing: -0.5px;
    line-height: 1.2;
    color: var(--navy);
    text-transform: uppercase;
    white-space: nowrap;
  }
  .agent-band {
    position: absolute;
    left: 0;
    top: 189px;
    width: 438px;
    height: 54px;
    background: linear-gradient(90deg, var(--band-dark), var(--band-light));
    box-shadow: 0 6px 6px rgba(0, 0, 0, 0.28);
    display: flex;
    align-items: center;
  }
  .agent-title {
    margin: 0 0 0 125px;
    font-family: "Open Sans", sans-serif;
    font-weight: 700;
    font-size: 24px;
    color: var(--white);
    text-transform: uppercase;
    white-space: nowrap;
  }
  .contact {
    position: absolute;
    left: 51px;
    top: 402px;
    margin: 0;
    padding: 0;
    list-style: none;
    font-family: "Open Sans", sans-serif;
    font-size: 25px;
    line-height: 32px;
    color: var(--ink);
    white-space: nowrap;
  }
</style>
</head>
<body>
  <article class="card">
    <svg class="card-art" viewBox="0 0 987 580">
      <defs>
        <linearGradient id="interiorTones" x1="0" y1="0" x2="0" y2="1">
          <stop offset="0" stop-color="var(--photo-light)"/>
          <stop offset="0.6" stop-color="var(--photo-mid)"/>
          <stop offset="0.75" stop-color="var(--photo-water)"/>
          <stop offset="1" stop-color="var(--photo-deep)"/>
        </linearGradient>
        <linearGradient id="swooshBlue" x1="0" y1="0" x2="0" y2="1">
          <stop offset="0" stop-color="var(--band-light)"/>
          <stop offset="1" stop-color="var(--band-dark)"/>
        </linearGradient>
      </defs>
      <rect class="interior-photo" x="0" y="0" width="987" height="580" fill="url(#interiorTones)" role="img" aria-label="Photograph of a bright modern living room with sofas, shelving and an indoor pool"/>
      <path class="swoosh-orange" d="M0 0 H665 C735 130 730 410 380 580 H0 Z" fill="var(--swoosh-orange)"/>
      <path class="swoosh-gap" d="M0 0 H625 C705 110 705 400 355 580 H0 Z" fill="var(--white)"/>
      <path class="swoosh-blue" d="M0 0 H600 C690 110 690 390 340 580 H0 Z" fill="url(#swooshBlue)"/>
      <path class="card-field" d="M0 0 H470 C620 70 650 350 300 580 H0 Z" fill="var(--white)"/>
    </svg>

    <h1 class="brand-name">Velmora Link5</h1>

    <div class="agent-band">
      <p class="agent-title">Mere Halani / Agent</p>
    </div>

    <ul class="contact">
      <li>License Number</li>
      <li>ABN Number</li>
      <li>Mobile: 0000000000</li>
      <li>Email: www.velmoralink5.co</li>
    </ul>
  </article>
</body>
</html>
```